Bright Lantern Studios Business Card Design

Doug Farley

Managing Partner

Doug@BrightLanternStudios.com

BrightLanternStudios.com

502-417-2356

Industry/Entity Type

Photographer

Contact Information for Business Card

Doug Farley

Managing Partner

Doug@BrightLanternStudios.com

BrightLanternStudios.com

502-417-2356

Requirements
Must have
• Must show that I am a pavlo trusted photographer

```html
<!DOCTYPE html>
<html lang="en">
<head>
<meta charset="utf-8">
<title>Bright Lantern Studios Business Card</title>
<link rel="stylesheet" href="https://fonts.googleapis.com/css2?family=Josefin+Sans:wght@400&family=Open+Sans:wght@400;600&display=swap">
<style>
  :root {
    --backdrop: #e9e7e4;
    --card-dark: #1e1e1e;
    --card-light: #ffffff;
    --ink-light: #ffffff;
    --ink-dark: #111111;
    --badge-fill: #d8d8d8;
  }
  * { margin: 0; padding: 0; box-sizing: border-box; }
  html, body {
    width: 1200px; height: 1000px; overflow: hidden;
    background: var(--backdrop);
  }
  .canvas { position: relative; width: 1200px; height: 1000px; }
  .card {
    position: absolute; left: 266px; width: 666px; height: 397px;
    box-shadow: 0 2px 6px rgba(0,0,0,0.25);
  }
  .card--front { top: 74px; background: var(--card-dark); }
  .card--back { top: 533px; background: var(--card-light); }

  .front-mark {
    position: absolute; left: 293px; top: 116px;
    width: 80px; height: 80px; border-radius: 50%;
    border: 9px solid var(--ink-light);
  }
  .front-wordmark {
    position: absolute; left: 0; right: 0; top: 234px;
    text-align: center; color: var(--ink-light);
    font-family: "Josefin Sans", sans-serif; font-weight: 400;
    font-size: 35px; letter-spacing: 0.5px;
  }

  .back-mark {
    position: absolute; left: 92px; top: 95px;
    width: 206px; height: 206px; border-radius: 50%;
    border: 18px solid var(--ink-dark);
    display: flex; align-items: center; justify-content: center;
  }
  .back-mark__name {
    font-family: "Open Sans", sans-serif; font-weight: 600;
    font-size: 15px; line-height: 1.25; text-align: center;
    color: var(--ink-dark); letter-spacing: 0.5px;
  }

  .contact {
    position: absolute; left: 364px; top: 102px;
    font-family: "Open Sans", sans-serif; color: var(--ink-dark);
  }
  .contact__name { font-weight: 600; font-size: 21px; letter-spacing: 0.4px; line-height: 1.2; }
  .contact__title { font-size: 16px; line-height: 1.3; }
  .contact__badge {
    display: block; width: 118px; height: 40px; margin: 14px 0 12px;
    background: var(--badge-fill); border-radius: 4px;
  }
  .contact__line { font-size: 16px; line-height: 25.5px; }
</style>
</head>
<body>
<main class="canvas">
  <section class="card card--front" aria-label="Card front">
    <div class="front-mark"></div>
    <p class="front-wordmark">BRIGHT LANTERN STUDIOS</p>
  </section>

  <section class="card card--back" aria-label="Card back">
    <div class="back-mark">
      <p class="back-mark__name">BRIGHT<br>LANTERN<br>STUDIOS</p>
    </div>
    <div class="contact">
      <p class="contact__name">DOUG FARLEY</p>
      <p class="contact__title">Managing Partner</p>
      <div class="contact__badge" role="img" aria-label="Pavlo trusted photographer badge"></div>
      <p class="contact__line">502-417-2356</p>
      <p class="contact__line">Doug@BrightLanternStudios.com</p>
      <p class="contact__line">BrightLanternStudios.com</p>
    </div>
  </section>
</main>
</body>
</html>
```